Business Card for Wellness Clinic

We need a business card for our new logo. I want it to match the feel of the logo

Target Market(s)

Young professional families looking for holistic health care

Industry/Entity Type

Health And Wellness

Contact Information for Business Card

Our business Name: Larkvale Health & wellness Centre, our phone #, email address...see attached old business card

Font styles to use
Sans Serif

Colors
33b8a4
cee9f5

Requirements
Must have
• my logo and business name
• Font is "Helvetica Neue LT Std 45 Light" and
• Only for "&" using font "Trajan pro bold"
• Use colors in the logo

```html
<!DOCTYPE html>
<html lang="en">
<head>
<meta charset="utf-8">
<title>Larkvale Health &amp; Wellness Centre – Business Cards</title>
<link rel="stylesheet" href="https://fonts.googleapis.com/css2?family=Roboto:wght@300;400;500&display=swap">
<style>
  :root {
    --teal: #33b8a4;
    --teal-dark: #1f9e8b;
    --ink: #0c0c0c;
    --paper: #ffffff;
    --paper-shade: #e9eaea;
    --grey-text: #8a8f91;
    --light-text: #d9dcdc;
    --backdrop: #1e1f20;
  }
  * { box-sizing: border-box; margin: 0; padding: 0; }
  html, body {
    width: 1200px; height: 997px; overflow: hidden;
    background: var(--backdrop);
    font-family: "Roboto", "Helvetica Neue", Arial, sans-serif;
    font-weight: 300;
  }
  .stage { position: relative; width: 1200px; height: 997px; }

  .card {
    position: absolute;
    width: 560px; height: 320px;
    background: var(--ink);
    overflow: hidden;
    box-shadow: 0 18px 40px rgba(0,0,0,.55);
  }
  .card--appointment { left: 70px; top: 110px; }
  .card--contact { left: 570px; top: 540px; }

  .card__band { position: absolute; inset: 0; width: 100%; height: 100%; }

  .brand {
    position: absolute; left: 0; right: 0; top: 46px;
    display: flex; align-items: center; justify-content: center; gap: 12px;
  }
  .brand__mark {
    width: 26px; height: 26px; background: var(--teal); border-radius: 4px;
  }
  .brand__name {
    color: var(--teal);
    font-weight: 300;
    font-size: 17px;
    letter-spacing: 3px;
    text-transform: uppercase;
    line-height: 1.35;
    text-align: center;
  }

  /* appointment side */
  .appt {
    position: absolute; left: 34px; right: 34px; top: 170px;
    color: var(--teal);
  }
  .appt__title { font-weight: 500; font-size: 14px; margin-bottom: 10px; }
  .appt__row { display: flex; gap: 26px; margin-bottom: 14px; }
  .appt__field {
    display: flex; align-items: flex-end; gap: 6px; font-size: 15px; flex: 1;
  }
  .appt__field span { text-decoration: underline; }
  .appt__line { flex: 1; border-bottom: 1px solid var(--teal); height: 1px; margin-bottom: 3px; }
  .appt__note { font-size: 9.5px; color: var(--teal); margin-top: 8px; }

  /* contact side */
  .person { position: absolute; left: 34px; top: 170px; }
  .person__name { color: var(--teal); font-size: 19px; font-weight: 400; }
  .person__title { color: var(--light-text); font-size: 11px; margin-top: 3px; }

  .contact-list { position: absolute; left: 34px; top: 228px; list-style: none; }
  .contact-list li {
    display: flex; align-items: center; gap: 10px;
    color: var(--light-text); font-size: 12.5px; margin-bottom: 6px;
  }
  .contact-list svg { width: 11px; height: 11px; fill: var(--teal); }

  .address {
    position: absolute; right: 30px; top: 168px; text-align: right;
    font-size: 11px; line-height: 1.45; color: var(--light-text);
  }
  .address__name { color: var(--teal); font-size: 12px; }
</style>
</head>
<body>
<main class="stage">

  <!-- Appointment card -->
  <section class="card card--appointment" aria-label="Appointment card">
    <svg class="card__band" viewBox="0 0 560 320" preserveAspectRatio="none" aria-hidden="true">
      <defs>
        <linearGradient id="paperA" x1="0" y1="0" x2="0" y2="1">
          <stop offset="0" stop-color="#ffffff"/>
          <stop offset="1" stop-color="#e6e8e8"/>
        </linearGradient>
      </defs>
      <rect x="0" y="0" width="560" height="150" fill="url(#paperA)"/>
      <polyline points="0,150 40,150 50,161 60,150 560,150" fill="none" stroke="#33b8a4" stroke-width="3"/>
      <line x1="0" y1="308" x2="560" y2="308" stroke="#33b8a4" stroke-width="3"/>
    </svg>
    <div class="brand">
      <span class="brand__mark"></span>
      <p class="brand__name">Larkvale Health &amp;<br>Wellness Centre</p>
    </div>
    <div class="appt">
      <p class="appt__title">Appointment Card</p>
      <div class="appt__row">
        <div class="appt__field"><span>Date:</span><i class="appt__line"></i></div>
        <div class="appt__field"><span>Time:</span><i class="appt__line"></i></div>
      </div>
      <div class="appt__row">
        <div class="appt__field"><span>For:</span><i class="appt__line"></i></div>
      </div>
      <p class="appt__note">If you are unable to keep your appointment, please provide at least 2 business days notice or full visit fees will apply.</p>
    </div>
  </section>

  <!-- Contact card -->
  <section class="card card--contact" aria-label="Business card">
    <svg class="card__band" viewBox="0 0 560 320" preserveAspectRatio="none" aria-hidden="true">
      <defs>
        <linearGradient id="paperB" x1="0" y1="0" x2="0" y2="1">
          <stop offset="0" stop-color="#ffffff"/>
          <stop offset="1" stop-color="#e6e8e8"/>
        </linearGradient>
      </defs>
      <rect x="0" y="0" width="560" height="150" fill="url(#paperB)"/>
      <polyline points="0,150 40,150 50,161 60,150 560,150" fill="none" stroke="#33b8a4" stroke-width="3"/>
      <line x1="0" y1="308" x2="560" y2="308" stroke="#33b8a4" stroke-width="3"/>
    </svg>
    <div class="brand">
      <span class="brand__mark"></span>
      <p class="brand__name">Larkvale Health &amp;<br>Wellness Centre</p>
    </div>

    <div class="person">
      <p class="person__name">Dr. Maren Holt, N.D</p>
      <p class="person__title">Naturopathic Doctor</p>
    </div>

    <ul class="contact-list">
      <li>
        <svg viewBox="0 0 12 12" aria-hidden="true"><rect x="3" y="0" width="6" height="12" rx="1"/></svg>
        613-555-0147
      </li>
      <li>
        <svg viewBox="0 0 12 12" aria-hidden="true"><rect x="0" y="2" width="12" height="8" rx="1"/></svg>
        mholt@larkvalenaturopathic.ca
      </li>
      <li>
        <svg viewBox="0 0 12 12" aria-hidden="true"><path d="M2 10 L9 1 L11 3 L4 12 L1 12 Z"/></svg>
        www.larkvalenaturopathic.ca
      </li>
    </ul>

    <address class="address">
      <span class="address__name">Larkvale Health &amp; Wellness Centre</span><br>
      48 Larkvale St. W, Suite 120<br>
      Ottawa, ON K1X 4B7
    </address>
  </section>

</main>
</body>
</html>
```